Wix website for a food and nutrition consultancy

Professional looking wix website design needed for a food and nutrition consulting service soon to be established in Australia.
Key services include nutrition research, food regulations compliance, in-house dietitian services, project management and food/nutrition advisory.

Target Market(s)

The market is B2B (ie business clients) particularly food manufacturers, food companies, corporate clients, restaurants (secondary), import/exporters etc.

Industry/Entity Type

Business Consultant

Logo Text

Bright Harvest Food & Nutrition Consulting

Number of Pages Required

4 page

Colors
f37022
ffc214
fbed22
03a68d
33a6d7

Requirements
Must have
• Needs to be modern and streamlined looking. An overall look that can be aligned with a logo and provide a strong brand image. Some pictures featuring a range of different food groups. A nice colour scheme...please use your creative insight to decide on which colours would work...I have picked a few but they are not must haves.
Nice to have
• More food pictures than people pictures please.
Should not have
• -

```html
<!DOCTYPE html>
<html lang="en">
<head>
<meta charset="utf-8">
<title>Bright Harvest Consulting</title>
<link href="https://fonts.googleapis.com/css2?family=Oswald:wght@400;500&family=Open+Sans:wght@400;600&display=swap" rel="stylesheet">
<style>
  :root {
    --black: #000000;
    --ink: #222222;
    --body: #666666;
    --orange: #e8652a;
    --blue: #33a6d7;
    --yellow: #ffc214;
    --teal: #1aab8e;
    --rule: #cfcfcf;
    --white: #ffffff;
  }
  * { margin: 0; padding: 0; box-sizing: border-box; }
  html, body { width: 1118px; height: 1200px; overflow: hidden; background: var(--white); }
  .page { position: relative; width: 1118px; height: 1200px; font-family: 'Open Sans', sans-serif; }
  .abs { position: absolute; }
  .display { font-family: 'Oswald', sans-serif; text-transform: uppercase; }

  .site-header { left: 0; top: 0; width: 1118px; height: 71px; background: var(--black); }
  .brand { left: 92px; top: 12px; color: var(--white); font-size: 19px; line-height: 24px; font-weight: 400; }
  .brand strong { font-weight: 500; }
  .nav { top: 23px; font-size: 16px; color: var(--white); line-height: 24px; }
  .nav.active { color: var(--orange); }
  .phone-ring { left: 889px; top: 21px; width: 29px; height: 29px; border: 1.5px solid var(--white); border-radius: 50%; }
  .phone-number { left: 927px; top: 23px; font-size: 18px; color: var(--white); line-height: 24px; }

  .photo { position: absolute; }
  .band { position: absolute; display: flex; align-items: center; justify-content: center; color: var(--white); font-family: 'Oswald', sans-serif; font-weight: 500; font-size: 21px; letter-spacing: 0.3px; text-transform: uppercase; }
  .band.blue { background: rgba(51,166,215,0.88); }
  .band.yellow { background: var(--yellow); }
  .band.orange { background: rgba(232,101,42,0.92); }
  .band.teal { background: rgba(26,171,142,0.9); }

  .welcome-kicker { left: 304px; top: 106px; font-size: 21px; color: var(--ink); line-height: 28px; }
  .welcome-title { left: 304px; top: 136px; width: 310px; font-size: 26px; color: var(--ink); font-weight: 500; line-height: 36px; white-space: nowrap; }
  .welcome-copy { left: 304px; top: 186px; width: 300px; font-size: 13px; line-height: 25.5px; color: var(--body); }
  .btn { position: absolute; height: 39px; border: 1px solid var(--body); border-radius: 3px; color: var(--orange); font-weight: 600; font-size: 14px; display: flex; align-items: center; justify-content: center; text-transform: uppercase; }

  .footer-brand { left: 90px; top: 978px; font-size: 32px; line-height: 38px; color: var(--ink); }
  .footer-title { top: 922px; font-size: 18px; color: var(--ink); font-weight: 500; line-height: 24px; }
  .footer-link { left: 332px; font-size: 11.5px; color: var(--body); line-height: 16px; }
  .footer-text { font-size: 11.5px; color: var(--body); line-height: 19px; }
  .email-field { left: 511px; top: 1017px; width: 237px; height: 26px; border-bottom: 1px solid var(--rule); font-size: 11px; color: #999; padding-left: 13px; line-height: 18px; }
  .subscribe { left: 511px; top: 1062px; width: 95px; height: 29px; border: 1px solid var(--orange); border-radius: 3px; color: var(--orange); font-size: 11.5px; display: flex; align-items: center; justify-content: center; }
  .icon { position: absolute; width: 14px; height: 14px; }
  .divider { left: 92px; top: 1136px; width: 935px; border-top: 1px solid var(--rule); }
  .copyright { left: 92px; top: 1158px; font-size: 11.5px; color: var(--body); }
  .social { position: absolute; top: 1155px; width: 24px; height: 24px; border: 1px solid var(--blue); border-radius: 50%; }
</style>
</head>
<body>
<div class="page">

  <header class="site-header abs">
    <div class="brand abs display">Bright Harvest<br><strong>Consulting</strong></div>
    <div class="nav abs display active" style="left:418px">Home</div>
    <div class="nav abs display" style="left:476px">About Us</div>
    <div class="nav abs display" style="left:557px">Nutrition Services</div>
    <div class="nav abs display" style="left:701px">Blog</div>
    <div class="nav abs display" style="left:755px">Contact Us</div>
    <svg class="abs" style="left:850px;top:29px" width="14" height="14" viewBox="0 0 14 14">
      <circle cx="5.5" cy="5.5" r="4.2" fill="none" stroke="#fff" stroke-width="2"/>
      <line x1="8.6" y1="8.6" x2="12.5" y2="12.5" stroke="#fff" stroke-width="2.2" stroke-linecap="round"/>
    </svg>
    <div class="phone-ring abs"></div>
    <svg class="abs" style="left:897px;top:29px" width="13" height="13" viewBox="0 0 24 24">
      <path fill="#e8652a" d="M6.6 10.8a15.1 15.1 0 0 0 6.6 6.6l2.2-2.2c.3-.3.7-.4 1-.2 1.1.4 2.3.6 3.6.6.6 0 1 .4 1 1V20c0 .6-.4 1-1 1A17 17 0 0 1 3 4c0-.6.4-1 1-1h3.5c.6 0 1 .4 1 1 0 1.3.2 2.5.6 3.6.1.3 0 .7-.2 1z"/>
    </svg>
    <div class="phone-number abs display">1 800 555 0134</div>
  </header>

  <div class="photo" role="img" aria-label="Toast topped with smashed avocado and halved soft-boiled eggs" style="left:0;top:74px;width:270px;height:316px;background:linear-gradient(150deg,#9b6a3c 0%,#8fae3d 35%,#f2e9da 55%,#f09a1e 65%,#7d5330 100%)"></div>

  <div class="welcome-kicker abs display">Welcome to</div>
  <div class="welcome-title abs display">Bright Harvest Consulting</div>
  <p class="welcome-copy abs">We are a food and nutrition consulting company in Australia. Nemo enim ipsam voluptatem quivo luptas sit aspernatur aut odit aut fugit, sed qu ia consequuntur magni dolores.</p>
  <div class="btn" style="left:304px;top:309px;width:136px">Get a Quote</div>
  <div class="btn" style="left:452px;top:309px;width:136px">Learn More</div>

  <div class="photo" role="img" aria-label="Grilled salmon fillets with asparagus and lemon slices" style="left:627px;top:71px;width:491px;height:319px;background:linear-gradient(160deg,#f4d2b8 0%,#ec8a4e 35%,#6fa341 60%,#f5d84a 80%,#f2efe8 100%)"></div>
  <div class="band blue" style="left:627px;top:153px;width:491px;height:49px">Food Regulations Compliance</div>

  <div class="photo" role="img" aria-label="Plate of spaghetti with grilled sausages" style="left:0;top:395px;width:317px;height:240px;background:linear-gradient(170deg,#6b3d1f 0%,#e49a3a 40%,#c8702a 70%,#4a2a18 100%)"></div>
  <div class="band blue" style="left:0;top:540px;width:317px;height:46px">Project Management</div>

  <div class="photo" role="img" aria-label="Berry smoothie in a glass beside oats and blueberries" style="left:0;top:635px;width:317px;height:241px;background:linear-gradient(160deg,#8a8480 0%,#b73f86 40%,#7d4a6a 70%,#3b3550 100%)"></div>
  <div class="band orange" style="left:0;top:786px;width:317px;height:46px">Nutrition Research</div>

  <div class="photo" role="img" aria-label="Assorted bread loaves and rolls in a basket with wheat ears" style="left:320px;top:395px;width:304px;height:481px;background:linear-gradient(180deg,#e3e3e5 0%,#d9d8da 30%,#9a6334 50%,#c88a4e 70%,#b9b3ad 100%)"></div>
  <div class="band yellow" style="left:320px;top:467px;width:304px;height:46px">Food/Nutrition Advisory</div>

  <div class="photo" role="img" aria-label="Citrus infused water with grapefruit, lemon, mint and strawberries" style="left:627px;top:395px;width:491px;height:481px;background:linear-gradient(150deg,#8a6a4a 0%,#f0a06a 30%,#f4d25a 55%,#e8552e 75%,#5a8a3a 100%)"></div>
  <div class="band teal" style="left:627px;top:710px;width:491px;height:50px">In-House Dietitian Services</div>

  <div class="footer-brand abs display">Bright Harvest<br>Consulting</div>

  <div class="footer-title abs display" style="left:332px">Information</div>
  <div class="footer-link abs" style="top:963px">Home</div>
  <div class="footer-link abs" style="top:989px">About Us</div>
  <div class="footer-link abs" style="top:1015px">Nutrition Services</div>
  <div class="footer-link abs" style="top:1042px">Blog</div>
  <div class="footer-link abs" style="top:1068px">Contact Us</div>

  <div class="footer-title abs display" style="left:511px">Newsletter Subscription</div>
  <div class="footer-text abs" style="left:511px;top:962px">Register your Email Address to get<br>Information about us</div>
  <div class="email-field abs">Email Address</div>
  <div class="subscribe abs">SUBSCRIBE</div>

  <div class="footer-title abs display" style="left:821px">Contact Us</div>
  <svg class="icon" style="left:821px;top:965px" viewBox="0 0 24 24"><path fill="#33a6d7" d="M12 2a7 7 0 0 0-7 7c0 5 7 13 7 13s7-8 7-13a7 7 0 0 0-7-7zm0 9.5A2.5 2.5 0 1 1 12 6.5a2.5 2.5 0 0 1 0 5z"/></svg>
  <div class="footer-text abs" style="left:849px;top:963px;line-height:17px">42 Harbour Lane #12<br>Sydney, NSW 2000 Australia</div>
  <svg class="icon" style="left:821px;top:1014px" viewBox="0 0 24 24"><path fill="#33a6d7" d="M6.6 10.8a15.1 15.1 0 0 0 6.6 6.6l2.2-2.2c.3-.3.7-.4 1-.2 1.1.4 2.3.6 3.6.6.6 0 1 .4 1 1V20c0 .6-.4 1-1 1A17 17 0 0 1 3 4c0-.6.4-1 1-1h3.5c.6 0 1 .4 1 1 0 1.3.2 2.5.6 3.6.1.3 0 .7-.2 1z"/></svg>
  <div class="footer-text abs" style="left:849px;top:1011px">1 800 555 0134</div>
  <svg class="icon" style="left:821px;top:1046px" viewBox="0 0 24 24"><rect x="6" y="2" width="12" height="6" fill="#33a6d7"/><rect x="3" y="9" width="18" height="13" rx="2" fill="#33a6d7"/><rect x="7" y="13" width="10" height="5" fill="#fff"/></svg>
  <div class="footer-text abs" style="left:849px;top:1043px">1 800 555 0178</div>
  <svg class="icon" style="left:821px;top:1079px" viewBox="0 0 24 24"><rect x="2" y="5" width="20" height="14" rx="1.5" fill="#33a6d7"/><path d="M2.5 6l9.5 7 9.5-7" fill="none" stroke="#fff" stroke-width="1.6"/></svg>
  <div class="footer-text abs" style="left:851px;top:1075px">info@brightharvestconsulting.com</div>

  <div class="divider abs"></div>
  <div class="copyright abs">Copyrights © 2017,Bright Harvest Consulting. All rights reserved. Terms &amp; Condition.</div>
  <div class="social" style="left:910px"></div>
  <div class="social" style="left:941px"></div>
  <div class="social" style="left:971px"></div>
  <div class="social" style="left:1001px"></div>

</div>
</body>
</html>
```